Home page for local retail aggregator

About us: We are a new company that showcases beautiful products available at nearby retail stores. This homepage is meant to display the latest products featured on our site and also allow the user to search, browse with filters, and access their account details.

Currently, our home page looks a little bland. We want the focus of the site to remain on the featured photos and products but the design should be more cohesive. The most successful designs will make more subtle use of our colors, provide intuitive menu controls, and look visually stunning.

This homepage has a few sections:

Header:
-Top Section: will always remain at the top of the page. There should be space for our company name ”zAntelope”, a tagline, and a place for the menus.
-Menus: user must be able to find links for: “My profile” “My Products” “Add Product” “Preview store”
-Bottom section: this will scroll with the user and always remain at the top of the screen providing access to a search box, and filters for “location” “price” and retail categories.

Main Page:
-Each product featured is shown on a tile that includes a photo, title, price, name of store, has space to leave a comment, and include counters for "likes," comments, and "Pods"). “Pods” are bookmark folders. The user’s profile pic is also shown in miniature if they leave a comment.

The final version of the site must be delivered in a fully layered photoshop file and have versions demonstrating what the page will look like both when a user is logged-in and when logged-out.

Target Market(s)

Most of our users are female 18-45. Our customers are retail store owners who want their products to look attractive and professional.

Industry/Entity Type

Retail

Requirements
Must have
• Our logo must be present on the site (attached to project). You're welcome to change the colors in the header but it should look good with our logo.

For reference here are colors we're currently using:
Site text is in Dark Blue: RGB(10/23/47)
Logo color on business cards is light blue: (51/153/204)
Nice to have
• Would love to see new versions of the menus that are more modern and intuitive. Currently we just have links to each individual control. Putting these in a drop-down or re-arranging them would be nice.

```html
<!DOCTYPE html>
<html lang="en">
<head>
<meta charset="utf-8">
<title>zAntelope – Local Product Search and Discovery</title>
<link href="https://fonts.googleapis.com/css2?family=Cabin:wght@400;500;600&display=swap" rel="stylesheet">
<style>
:root{
  --ink:#0a172f;
  --muted:#8a9096;
  --page:#e4f3f3;
  --band:#aacbea;
  --brand:#3399cc;
  --tile:#f4f5f5;
  --tile-line:#d5dbdb;
  --tag:#9aa3a3;
  --join:#7bb7e4;
  --social:#b7d5f0;
}
*{box-sizing:border-box;margin:0;padding:0}
html,body{width:1200px;height:1029px;overflow:hidden;background:var(--page)}
body{font-family:"Cabin",sans-serif;color:var(--ink)}
.stage{width:1100px;height:943px;position:relative;overflow:hidden;transform:scale(1.090909);transform-origin:0 0;background:var(--page)}

/* header */
.masthead{position:absolute;left:0;top:0;width:1100px;height:65px}
.brand-mark{position:absolute;left:108px;top:8px;width:68px;height:68px;border-radius:50%;background:var(--brand)}
.brand-name{position:absolute;left:190px;top:4px;font-size:25px;font-weight:600;letter-spacing:2px;color:var(--ink)}
.tagline{position:absolute;left:190px;top:36px;font-size:15.5px;letter-spacing:.6px;color:#2a3444;border-top:1px solid #5d6a7a;padding-top:2px}
.account-menu{position:absolute;left:600px;top:4px;display:flex;list-style:none}
.account-menu li{height:58px;display:flex;flex-direction:column;align-items:center;justify-content:flex-end;padding:0 6px;border-left:1px solid #c9d6d6;font-size:14px}
.account-menu li:first-child{border-left:none}
.account-menu svg{margin-bottom:2px}

.search-band{position:absolute;left:0;top:65px;width:1100px;height:86px;background:var(--band)}
.search-title{position:absolute;left:235px;top:8px;font-size:16px;letter-spacing:.6px;text-decoration:underline;text-underline-offset:3px}
.filter{position:absolute;top:34px;height:32px;background:#e6e9ec;border:1px solid #c5cdd6;border-radius:3px;box-shadow:inset 0 1px 2px #fff;display:flex;align-items:center}
.filter span{flex:1;text-align:center;font-size:11px;letter-spacing:.5px;color:#3a4250}
.filter .drop{width:26px;height:22px;margin-right:6px;background:#3a8fd0;border-radius:2px;display:flex;align-items:center;justify-content:center}
.filter .lens{margin-left:10px}

/* auth */
.btn{position:absolute;top:167px;height:36px;display:flex;align-items:center;justify-content:center;font-size:14px;border-radius:2px}
.btn-join{left:793px;width:136px;background:var(--join);color:#fff;font-weight:600;border:1px solid #6aa6d4}
.btn-login{left:935px;width:78px;background:#f1f1f1;color:var(--ink);border:1px solid #c8c8c8;box-shadow:0 2px 3px rgba(0,0,0,.2)}

/* social rail */
.social-rail{position:absolute;left:0;top:355px;width:64px;height:157px;background:var(--social)}
.social-rail a{position:absolute;left:10px;width:44px;height:44px;border-radius:50%;background:#fff;color:var(--brand);font-size:8px;display:flex;align-items:center;justify-content:center;text-decoration:none}

/* tiles */
.tile{position:absolute;background:var(--tile);border:1px solid var(--tile-line);padding:7px 7px 0}
.photo{width:100%}
.meta{position:relative;padding:6px 44px 4px 2px;font-size:12.5px;letter-spacing:.6px;line-height:14px}
.price{position:absolute;right:-10px;top:6px;background:var(--tag);color:#fff;font-size:11px;padding:1px 5px;min-width:36px;text-align:right}
.stats{display:flex;gap:16px;font-size:9px;color:var(--muted);padding:4px 0 4px;border-bottom:1px solid #dde2e2;letter-spacing:.3px}
.note{display:flex;gap:6px;align-items:flex-start;padding:5px 0;border-bottom:1px solid #dde2e2;font-size:8px;line-height:12px}
.avatar{flex:none;width:20px;height:20px;background:linear-gradient(#c79a7e,#6b4a3a)}
.reply{display:flex;align-items:center;gap:8px;padding:5px 0 6px}
.reply .dot{width:14px;height:14px;border-radius:50%;background:#c6cbcb;flex:none;margin-left:4px}
.reply .field{flex:1;height:20px;border:1px solid #ccd2d2;background:#fbfbfb;font-size:8px;color:#6a7178;display:flex;align-items:center;justify-content:center;letter-spacing:.4px}

.to-top{position:absolute;left:957px;top:862px;width:60px;height:58px;background:#e6e8e8;border:1px solid #c6c6c6;box-shadow:0 2px 5px rgba(0,0,0,.3);font-size:12px;text-align:center;line-height:15px;padding-top:9px}
</style>
</head>
<body>
<div class="stage">

  <header class="masthead">
    <div class="brand-mark"></div>
    <div class="brand-name">zAntelope</div>
    <div class="tagline">Local Product Search and Discovery</div>
    <ul class="account-menu">
      <li><svg width="30" height="34" viewBox="0 0 30 34"><circle cx="15" cy="9" r="8" fill="#5b1d6d"/><path d="M3 34 Q5 16 15 16 Q25 16 27 34Z" fill="#5b1d6d"/></svg>My Profile</li>
      <li><svg width="50" height="40" viewBox="0 0 50 40"><path d="M6 12h22v28H6z" fill="#d92020"/><path d="M11 12q0-10 6-10t6 10" fill="none" stroke="#555" stroke-width="2"/><path d="M26 18h20v22H26z" fill="#2a9fd6"/><path d="M30 18q0-8 6-8t6 8" fill="none" stroke="#555" stroke-width="2"/></svg>My Products</li>
      <li><svg width="44" height="40" viewBox="0 0 44 40"><circle cx="24" cy="20" r="18" fill="#55c840"/><path d="M8 14h8v-8h10v8h8v10h-8v8H16v-8H8z" fill="#cfd6cf" stroke="#999"/></svg>Add Products</li>
      <li><svg width="60" height="36" viewBox="0 0 60 36"><path d="M2 18Q30-6 58 18Q30 42 2 18Z" fill="#fff" stroke="#2aa7e0" stroke-width="3"/><circle cx="30" cy="18" r="10" fill="#2aa7e0"/><circle cx="30" cy="18" r="5" fill="#0a2a55"/></svg>Preview Products</li>
    </ul>
  </header>

  <section class="search-band">
    <div class="search-title">Search Products ›</div>
    <div class="filter" style="left:233px;width:254px"><svg class="lens" width="26" height="22" viewBox="0 0 26 22"><circle cx="10" cy="9" r="7" fill="none" stroke="#8d959e" stroke-width="2"/><path d="M15 14l8 6" stroke="#8d959e" stroke-width="3"/></svg><span>..........By Location............</span><div class="drop"><svg width="12" height="12" viewBox="0 0 12 12"><path d="M1 2l5 4 5-4M1 6l5 4 5-4" fill="none" stroke="#fff" stroke-width="1.6"/></svg></div></div>
    <div class="filter" style="left:500px;width:250px"><svg class="lens" width="26" height="22" viewBox="0 0 26 22"><circle cx="10" cy="9" r="7" fill="none" stroke="#8d959e" stroke-width="2"/><path d="M15 14l8 6" stroke="#8d959e" stroke-width="3"/></svg><span>..........By Price $............</span><div class="drop"><svg width="12" height="12" viewBox="0 0 12 12"><path d="M1 2l5 4 5-4M1 6l5 4 5-4" fill="none" stroke="#fff" stroke-width="1.6"/></svg></div></div>
    <div class="filter" style="left:763px;width:254px"><svg class="lens" width="26" height="22" viewBox="0 0 26 22"><circle cx="10" cy="9" r="7" fill="none" stroke="#8d959e" stroke-width="2"/><path d="M15 14l8 6" stroke="#8d959e" stroke-width="3"/></svg><span>..........By Product............</span><div class="drop"><svg width="12" height="12" viewBox="0 0 12 12"><path d="M1 2l5 4 5-4M1 6l5 4 5-4" fill="none" stroke="#fff" stroke-width="1.6"/></svg></div></div>
  </section>

  <a class="btn btn-join">Join zAntelope »</a>
  <a class="btn btn-login">Login</a>

  <nav class="social-rail">
    <a style="top:23px">Circlely</a>
    <a style="top:86px">Chirper</a>
  </nav>

  <!-- column 1 -->
  <article class="tile" style="left:79px;top:217px;width:176px">
    <div class="photo" role="img" aria-label="Copper ring with a rough-cut stone" style="height:152px;background:linear-gradient(135deg,#7a6d66,#3f3a38)"></div>
    <div class="meta">Right Finger Ring<span class="price">$50</span></div>
    <div class="stats"><span>1 Like</span><span>1 Comment</span><span>0 Pod</span></div>
    <div class="note"><div class="avatar" role="img" aria-label="Commenter profile picture"></div><p>Mara Linden love the rough cut of this</p></div>
    <div class="reply"><span class="dot"></span><span class="field">Leave Your Comment</span></div>
  </article>
  <article class="tile" style="left:79px;top:497px;width:176px">
    <div class="photo" role="img" aria-label="Woman wearing a colourful printed top" style="height:200px;background:linear-gradient(#e9ddd6,#c0578c 55%,#e04f8f)"></div>
    <div class="meta" style="padding-top:14px;padding-bottom:10px">Casual Tops<span class="price" style="top:14px">$8</span></div>
    <div class="stats"><span>25 Likes</span><span>0 Comments</span><span>6Pods</span></div>
    <div class="reply"><span class="dot"></span><span class="field">Leave Your Comment</span></div>
  </article>
  <article class="tile" style="left:79px;top:820px;width:176px">
    <div class="photo" role="img" aria-label="Layered chocolate dessert" style="height:140px;background:linear-gradient(#7a5236,#3e2a1c)"></div>
  </article>

  <!-- column 2 -->
  <article class="tile" style="left:266px;top:217px;width:177px">
    <div class="photo" role="img" aria-label="Chocolate chip cookies on a checked cloth" style="height:148px;background:linear-gradient(135deg,#e2c47e,#c99a4f)"></div>
    <div class="meta">Chocolate Chip Pudding Cookies<span class="price">$5</span></div>
    <div class="stats"><span>0 Like</span><span>0 Comment</span><span>0 Pod</span></div>
    <div class="reply"><span class="dot"></span><span class="field">Leave Your Comment</span></div>
  </article>
  <article class="tile" style="left:266px;top:482px;width:177px">
    <div class="photo" role="img" aria-label="Wooden spoons with colourful painted handles" style="height:140px;background:linear-gradient(90deg,#c99e78,#e8cfb4 40%,#9ed17c 70%,#b591d6)"></div>
    <div class="meta">Painted Kitchen Spoons<span class="price">$3</span></div>
    <div class="stats"><span>2 Likes</span><span>1 Comment</span><span>2Pods</span></div>
    <div class="note"><div class="avatar" role="img" aria-label="Commenter profile picture"></div><p>Mara Linden love the rough cut of this</p></div>
    <div class="reply"><span class="dot"></span><span class="field">Leave Your Comment</span></div>
  </article>
  <article class="tile" style="left:266px;top:777px;width:177px">
    <div class="photo" role="img" aria-label="Floral nightgowns for girls" style="height:142px;background:linear-gradient(90deg,#c7b7c2,#e9e1e4 50%,#e889b6)"></div>
    <div class="meta">Painted Kitchen</div>
  </article>

  <!-- column 3 -->
  <article class="tile" style="left:453px;top:217px;width:189px">
    <div class="photo" role="img" aria-label="Gold photo frame holding a to-do list" style="height:262px;background:linear-gradient(#f3f1ea 0 8%,#c9a634 8% 20%,#2f3a48 20% 85%,#c9a634 85% 92%,#3a3630 92%)"></div>
    <div class="meta" style="padding-top:10px">Classic Photo Frame<span class="price" style="top:10px">$35</span></div>
    <div class="stats"><span>6 Likes</span><span>2 Comments</span><span>0 Pod</span></div>
    <div class="note"><div class="avatar" role="img" aria-label="Commenter profile picture"></div><p>Mara Linden love the rough cut of this</p></div>
    <div class="note"><div class="avatar" role="img" aria-label="Commenter profile picture"></div><p>Mara Linden love the rough cut of this</p></div>
    <div class="reply"><span class="dot"></span><span class="field">Leave Your Comment</span></div>
  </article>
  <article class="tile" style="left:453px;top:655px;width:189px">
    <div class="photo" role="img" aria-label="Gold and silver two-finger rings" style="height:150px;background:linear-gradient(135deg,#f2f1ee,#d8c466 45%,#b9bcbd 70%,#ecebe8)"></div>
    <div class="meta" style="padding-top:10px;padding-bottom:12px">2 Finger Rings<span class="price" style="top:10px">$300</span></div>
    <div class="stats"><span>0 Like</span><span>0 Comment</span><span>0 Pod</span></div>
    <div class="reply"><span class="dot"></span><span class="field">Leave Your Comment</span></div>
  </article>
  <article class="tile" style="left:453px;top:920px;width:189px">
    <div class="photo" role="img" aria-label="Evening dresses" style="height:40px;background:linear-gradient(90deg,#6b2030,#2a2226)"></div>
  </article>

  <!-- column 4 -->
  <article class="tile" style="left:653px;top:217px;width:177px">
    <div class="photo" role="img" aria-label="Woman in a red sweater and black capris" style="height:198px;background:linear-gradient(#f1ece7 40%,#d33a36 55%,#2e2e34 75%,#efe9e4)"></div>
    <div class="meta" style="padding-top:14px">Beautiful Ladies Outfit<span class="price" style="top:14px">$35</span></div>
    <div class="stats"><span>25 Likes</span><span>0 Comments</span><span>6Pods</span></div>
    <div class="reply"><span class="dot"></span><span class="field">Leave Your Comment</span></div>
  </article>
  <article class="tile" style="left:653px;top:540px;width:177px">
    <div class="photo" role="img" aria-label="White ruffled fleece scarf with denim jacket" style="height:190px;background:linear-gradient(90deg,#34455c,#f2f2f2 35% 70%,#34455c)"></div>
    <div class="meta">Fleece Scarf<span class="price">$3.5</span></div>
    <div class="stats"><span>2 Likes</span><span>1 Comment</span><span>2Pods</span></div>
    <div class="note"><div class="avatar" role="img" aria-label="Commenter profile picture"></div><p>Mara Linden love the rough cut of this</p></div>
    <div class="reply"><span class="dot"></span><span class="field">Leave Your Comment</span></div>
  </article>
  <article class="tile" style="left:653px;top:866px;width:177px">
    <div class="photo" role="img" aria-label="Light blue shell-shaped soaps" style="height:80px;background:linear-gradient(#e6f3f5,#a9dde6)"></div>
  </article>

  <!-- column 5 -->
  <article class="tile" style="left:839px;top:217px;width:178px">
    <div class="photo" role="img" aria-label="Cream kitchen with tiled backsplash" style="height:190px;background:linear-gradient(#efeadf,#d8cfb8 50%,#b8ae98)"></div>
    <div class="meta">Kitchen Complete<span class="price">$35</span></div>
    <div class="stats"><span>2 Likes</span><span>1 Comment</span><span>2Pods</span></div>
    <div class="note"><div class="avatar" role="img" aria-label="Commenter profile picture"></div><p>Mara Linden love the rough cut of this</p></div>
    <div class="reply"><span class="dot"></span><span class="field">Leave Your Comment</span></div>
  </article>
  <article class="tile" style="left:839px;top:543px;width:178px">
    <div class="photo" role="img" aria-label="Emerald-cut diamond ring" style="height:188px;background:radial-gradient(#fbfbfb,#c9c9c9)"></div>
    <div class="meta" style="padding-top:10px">Antique Diamond Ring<span class="price" style="top:10px">$3.5</span></div>
    <div class="stats"><span>2 Likes</span><span>1 Comment</span><span>2Pods</span></div>
    <div class="note"><div class="avatar" role="img" aria-label="Commenter profile picture"></div><p>Mara Linden love the rough cut of this</p></div>
    <div class="reply"><span class="dot"></span><span class="field">Leave Your Comment</span></div>
  </article>
  <article class="tile" style="left:839px;top:887px;width:178px">
    <div class="photo" role="img" aria-label="Black smartphone" style="height:60px;background:linear-gradient(#e8e8e8,#555 60%)"></div>
  </article>

  <a class="to-top">Scroll<br>To<br>Top ▲</a>
</div>
</body>
</html>
```